Business Card Design Project

Build kick ass business card.
Updates

I just uploaded the Vorintex Logo in AI format, for those that were asking. It's looking real good and we'll be reviewing the designs soon. Thanks. 

Target Market(s)

Businesses in many verticals. Focusing on information security.

Vorintex, LLC
Gordon Bexley
Principal Security Consultant
Mobile: +1-602-555-0187
Email: Gordon.Bexley@Vorintex.example
Web: www.vorintex.example

Industry/Entity Type

Business

Requirements
Must have
• Design must look high-end, hi-tech stylish and minimalist

Be different – one that stands out from thousands of others

Does not have to be traditional rectangle

Would like logo integrated

```html
<!DOCTYPE html>
<html lang="en">
<head>
<meta charset="utf-8">
<title>Vorintex, LLC – Business Card</title>
<link rel="stylesheet" href="https://fonts.googleapis.com/css2?family=Arimo:wght@400&family=Libre+Baskerville:wght@700&family=Playfair+Display:ital,wght@1,500&display=swap">
<style>
  :root {
    --card-red: #99061f;
    --swoosh-white: #ffffff;
    --swoosh-pink: #b03a52;
    --text-light: #ffffff;
    --text-dark: #1f1f1f;
    --mark-blue: #3c9ad0;
    --frame: #9a9a9a;
  }
  html, body {
    margin: 0;
    padding: 0;
    width: 1200px;
    height: 770px;
    overflow: hidden;
    background: #ffffff;
  }
  .business-card {
    position: relative;
    width: 1200px;
    height: 770px;
    background: var(--card-red);
    box-sizing: border-box;
    border: 1px solid var(--frame);
    overflow: hidden;
  }
  .swoosh {
    position: absolute;
    inset: 0;
    width: 100%;
    height: 100%;
  }
  .brand {
    position: absolute;
    left: 640px;
    top: 150px;
    display: flex;
    align-items: center;
    gap: 26px;
  }
  .brand-mark {
    width: 110px;
    height: 110px;
    background: var(--mark-blue);
  }
  .brand-text {
    display: flex;
    flex-direction: column;
  }
  .brand-name {
    font-family: "Arimo", Arial, sans-serif;
    font-weight: 400;
    font-size: 60px;
    line-height: 1;
    letter-spacing: 1px;
    color: var(--text-dark);
  }
  .brand-tagline {
    font-family: "Arimo", Arial, sans-serif;
    font-weight: 400;
    font-size: 24px;
    margin-top: 10px;
    color: #333333;
  }
  .identity {
    position: absolute;
    left: 78px;
    top: 180px;
    margin: 0;
    font-family: "Playfair Display", Georgia, serif;
    font-style: italic;
    font-weight: 500;
    font-size: 29px;
    line-height: 44px;
    color: var(--text-light);
  }
  .contact {
    position: absolute;
    left: 132px;
    top: 652px;
    margin: 0;
    font-family: "Libre Baskerville", Georgia, serif;
    font-weight: 700;
    font-size: 24px;
    line-height: 40px;
    color: var(--text-light);
  }
</style>
</head>
<body>
  <div class="business-card">
    <svg class="swoosh" viewBox="0 0 1200 770" aria-hidden="true">
      <defs>
        <linearGradient id="swooshFill" x1="0.35" y1="0.3" x2="1" y2="1">
          <stop offset="0" stop-color="var(--swoosh-white)"/>
          <stop offset="0.45" stop-color="var(--swoosh-white)"/>
          <stop offset="1" stop-color="var(--swoosh-pink)"/>
        </linearGradient>
      </defs>
      <path d="M487,0 C440,110 470,250 600,330 C720,400 860,390 960,450 C1080,520 1170,640 1195,770 L1200,770 L1200,0 Z"
            fill="url(#swooshFill)" stroke="#ffffff" stroke-width="1.5"/>
    </svg>

    <div class="brand">
      <div class="brand-mark"></div>
      <div class="brand-text">
        <span class="brand-name">VORINTEX</span>
        <span class="brand-tagline">network security solutions</span>
      </div>
    </div>

    <p class="identity">
      Vorintex, LLC<br>
      Gordon Bexley<br>
      Principal Security Consultant
    </p>

    <p class="contact">
      Mobile: +1-602-555-0187, Email: Gordon.Bexley@Vorintex.example<br>
      Web: www.vorintex.example
    </p>
  </div>
</body>
</html>
```